Front & Back Book Cover Design

Title:
THE QUIET LANDLORD: How to Grow Comfort and Plenty Through Property Held by Others
Author:
Mel T. Varnak
Design Philosophy:
A modern, minimalist-luxury aesthetic that feels visionary and intelligent — positioned between business innovation (The Brisk Venture), modern finance (The Anatomy of Thrift), and timeless real estate insight (Bold Aunt Meek Aunt).
Think: clean, bold, and idea-driven — a visual reflection of the book’s central concept: wealth through clarity, not clutter.
Back Cover:
To include book description along with author photo and bio
Files:
PNG, PDF, EPUB

```html
<!DOCTYPE html>
<html lang="en">
<head>
<meta charset="UTF-8">
<title>The Quiet Landlord — Book Cover</title>
<link href="https://fonts.googleapis.com/css2?family=Arimo:wght@400;700&family=Crimson+Pro:ital,wght@1,500;0,700&family=Josefin+Sans:wght@600&family=Cinzel:wght@700&display=swap" rel="stylesheet">
<style>
  :root {
    --paper: #ffffff;
    --ink: #111111;
    --gold: #b98b47;
    --jacket-dark: #1b2226;
    --jacket-mid: #3a4247;
    --shirt: #eeeeee;
    --portrait-dark: #1e1f22;
    --portrait-mid: #4a4d52;
  }
  * { margin: 0; padding: 0; box-sizing: border-box; }
  html, body { width: 1200px; height: 900px; overflow: hidden; background: var(--paper); }
  .cover { position: relative; width: 1200px; height: 900px; background: var(--paper); color: var(--ink); }

  /* Back cover */
  .back { position: absolute; left: 50px; top: 38px; width: 485px; font-family: "Arimo", Helvetica, Arial, sans-serif; font-size: 14.6px; line-height: 18.5px; }
  .back p { text-align: justify; }
  .back-title { font-weight: 700; }
  .back-intro { margin-top: 20px; }
  .discover-heading { font-weight: 700; margin-top: 12px; }
  .benefits { list-style: none; margin-top: 9px; }
  .benefits li { text-align: justify; margin-bottom: 5px; }
  .benefits li::before { content: "• "; }
  .closing { margin-top: 10px; }
  .tagline { position: absolute; left: 50px; top: 607px; width: 485px; text-align: center; font-family: "Arimo", Helvetica, Arial, sans-serif; font-size: 14.6px; line-height: 18.5px; }
  .tagline strong { font-weight: 700; }

  .author-photo { position: absolute; left: 49px; top: 695px; width: 169px; height: 169px; border-radius: 20px 0 20px 0;
    background: radial-gradient(circle at 50% 40%, var(--portrait-mid), var(--portrait-dark) 75%); }
  .bio { position: absolute; left: 242px; top: 696px; width: 292px; font-family: "Arimo", Helvetica, Arial, sans-serif; font-size: 14.6px; line-height: 19.8px; text-align: justify; }
  .bio-name { font-weight: 700; font-variant: small-caps; }

  /* Front cover */
  .front-title { position: absolute; left: 684px; top: 18px; width: 460px; font-family: "Crimson Pro", Georgia, serif; color: var(--gold); line-height: 1; }
  .title-the { display: block; font-style: italic; font-weight: 500; font-size: 66px; line-height: 56px; }
  .title-quiet { display: block; font-weight: 700; font-size: 96px; line-height: 74px; letter-spacing: 6px; }
  .title-landlord { display: block; font-weight: 700; font-size: 122px; line-height: 100px; letter-spacing: -1px; }
  .subtitle { position: absolute; left: 676px; top: 258px; width: 460px; font-family: "Josefin Sans", Arial, sans-serif; font-weight: 600; font-variant: small-caps; font-size: 25px; line-height: 32px; text-align: center; letter-spacing: 1px; color: var(--ink); }
  .glasses-mark { position: absolute; left: 880px; top: 340px; width: 88px; height: 28px; border-radius: 4px 4px 14px 14px; background: var(--ink); }
  .jacket-figure { position: absolute; left: 698px; top: 420px; width: 441px; height: 408px;
    background: linear-gradient(90deg, var(--jacket-dark) 0%, var(--jacket-mid) 32%, var(--shirt) 42%, var(--shirt) 58%, var(--jacket-mid) 68%, var(--jacket-dark) 100%); }
  .author-name { position: absolute; left: 700px; top: 830px; width: 460px; text-align: center; font-family: "Cinzel", Georgia, serif; font-weight: 700; font-size: 44px; letter-spacing: 1px; color: var(--ink); }
  .author-name .initial { color: var(--gold); font-size: 56px; }
</style>
</head>
<body>
<main class="cover">
  <section class="back">
    <p class="back-title">THE QUIET LANDLORD</p>
    <p>How to Grow Comfort and Plenty Through Property Held by Others</p>
    <p>by Mel T. Varnak</p>

    <p class="back-intro">What if the smartest real estate investors in the world don’t actually own anything?<br>
    In a world where leverage has replaced labor and access has replaced assets, The Quiet Landlord reveals how a new generation of entrepreneurs is building wealth without deeds, mortgages, or massive capital.<br>
    Mel T. Varnak exposes the hidden playbook behind modern real estate wealth — not through ownership, but through control, creativity, and influence.</p>

    <p class="discover-heading">You’ll discover how to:</p>
    <ul class="benefits">
      <li>Profit from properties you never buy through partnerships, performance models, and control agreements.</li>
      <li>Monetize your skills, systems, and relationships just like institutional investors do.</li>
      <li>Build digital real estate — brands, websites, and lead funnels that pay like rentals.</li>
      <li>Create recurring income through master leases, management contracts, and service-based equity.</li>
    </ul>

    <p class="closing">Design your freedom formula — where wealth is measured in time, not titles.<br>
    Packed with frameworks, examples, and the mindset of modern deal-makers, <strong>The Quiet Landlord</strong> is a blueprint for the future of wealth creation — one built on access, not assets.</p>
  </section>

  <p class="tagline">Because in the new economy, the most powerful investors don’t own<br>real estate. They own opportunity.<br><strong>AND NOW, YOU CAN TOO.</strong></p>

  <div class="author-photo" role="img" aria-label="Portrait photo of the author in a grey blazer, arms crossed, against a dark background"></div>
  <p class="bio"><span class="bio-name">Mel T. Varnak</span> is a real estate entrepreneur and owner of HALVERLY Studio in Las Vegas, NV and Crestline Home Partners in Ventura, California. Combining design, development, and deal strategy, he’s helped agents, investors, and entrepreneurs build freedom through systems — not stuff. The Quiet Landlord is his definitive guide to building wealth through creative control.</p>

  <h1 class="front-title">
    <span class="title-the">The</span>
    <span class="title-quiet">QUIET</span>
    <span class="title-landlord">Landlord</span>
  </h1>
  <p class="subtitle">How to Grow Comfort and Plenty<br>Through Property Held by Others</p>
  <div class="glasses-mark" role="img" aria-label="Small black eyeglasses icon with mountains reflected in the lenses"></div>
  <div class="jacket-figure" role="img" aria-label="Photo of a headless figure wearing a black blazer over a white t-shirt"></div>
  <p class="author-name"><span class="initial">M</span>EL <span class="initial">T</span>. <span class="initial">V</span>ARNAK</p>
</main>
</body>
</html>
```